Stage Design Company Business Card

We are looking to step up up our business card design for our team.

We are a Full service Design and Consultation company for Stage and TV with an emphasis in Theatrical Lighting.

We like our materials to be clean and modern with solid colors free of patterns and gradients. Our brand consists of 4 primary colors Purple, Black, Grey, and White. Provided is our Word Mark as well as our Symbol Logo.

We would like our cards to leave an impression beyond the information, show our attention to design and detail, and make our marks an easily recognized feature (together or apart) for our clients.

We need a warm approachable comfortable feel for some clients, and a professional flair for the board member type clients.

Attached are our brand elements, and our existing cards to give a sense of our style and a glipse at the information we provide on our cards.

Target Market(s)

broad client base from church leaders to high school teachers and architects.

Industry/Entity Type

Business

Contact Information for Business Card

We format our phone number with periods not parenthesis or dashes. Information will be edited for each of our team members, and team member specific cards are not part of this scope, but rather a template so to speak.

Font styles to use
Sans Serif

Colors
6b449b
ffffff
000000
333333
aaaaaa

Requirements
Must have
• Wordmark and logo mark present (does not need to exist on the same side of card)
• Brand Colors,
• Name, Phone, Email, Address.
• Unique choices that make someone stop and take a second look
Nice to have
• It would be nice to somehow convey what we DO, as our brand name does not lend itself to this, outside of an obvious tagline though.....
• social media if not crowded. all of our handles match (instagram, twitter, facebook)
Should not have
• "clipart"

```html
<!DOCTYPE html>
<html lang="en">
<head>
<meta charset="utf-8">
<title>Lumen Entertainment – Business Card</title>
<link rel="stylesheet" href="https://fonts.googleapis.com/css2?family=Jost:wght@300;400;500;600&display=swap">
<style>
  :root {
    --purple: #372866;
    --white: #ffffff;
    --ink: #1c1c1c;
    --grey-light: #aaaaaa;
    --backdrop: #dcdcde;
  }
  * { box-sizing: border-box; margin: 0; padding: 0; }
  html, body { width: 1200px; height: 809px; overflow: hidden; }
  body {
    background: var(--backdrop);
    font-family: "Jost", sans-serif;
    position: relative;
  }
  .card {
    position: absolute;
    top: 114px;
    width: 320px;
    height: 580px;
    box-shadow: 0 6px 18px rgba(0,0,0,0.18);
    overflow: hidden;
  }
  .card--front { left: 230px; background: var(--white); }
  .card--back  { left: 650px; background: var(--purple); }

  .brand {
    position: absolute;
    top: 90px;
    left: 0;
    width: 100%;
    display: flex;
    flex-direction: column;
    align-items: center;
    font-weight: 500;
  }
  .brand__dot {
    width: 96px;
    height: 96px;
    border-radius: 50%;
    margin-bottom: 44px;
  }
  .brand__name {
    font-size: 30px;
    letter-spacing: 0.42em;
    padding-left: 0.42em;
    line-height: 1;
  }
  .brand__tagline {
    margin-top: 12px;
    font-size: 8px;
    letter-spacing: 0.62em;
    padding-left: 0.62em;
  }
  .card--front .brand { color: var(--ink); }
  .card--front .brand__dot { background: var(--purple); }
  .card--back .brand { color: var(--white); }
  .card--back .brand__dot { background: var(--white); }

  .holder-name {
    position: absolute;
    left: 26px;
    top: 392px;
    font-size: 22px;
    font-weight: 600;
    letter-spacing: 0.04em;
    color: var(--purple);
  }
  .contact-band {
    position: absolute;
    left: 0;
    bottom: 0;
    width: 100%;
    height: 134px;
    background: var(--purple);
    padding: 22px 26px 0;
    color: var(--white);
    font-size: 15px;
    font-weight: 300;
    line-height: 1.55;
    letter-spacing: 0.02em;
  }
  .social {
    position: absolute;
    left: 0;
    bottom: 36px;
    width: 100%;
    display: flex;
    justify-content: space-between;
    padding: 0 34px;
  }
  .social__dot {
    width: 18px;
    height: 18px;
    border-radius: 50%;
    background: var(--white);
    opacity: 0.85;
  }
</style>
</head>
<body>
  <section class="card card--front" aria-label="Card front">
    <div class="brand">
      <span class="brand__dot"></span>
      <span class="brand__name">LUMEN</span>
      <span class="brand__tagline">ENTERTAINMENT</span>
    </div>
    <h1 class="holder-name">REED A CARVER</h1>
    <address class="contact-band" style="font-style:normal">
      480.555.0147<br>
      REED@LUMEN-E.COM<br>
      52 W OAK ST TEMPE, AZ 85281
    </address>
  </section>

  <section class="card card--back" aria-label="Card back">
    <div class="brand">
      <span class="brand__dot"></span>
      <span class="brand__name">LUMEN</span>
      <span class="brand__tagline">ENTERTAINMENT</span>
    </div>
    <div class="social" aria-label="Social media">
      <span class="social__dot"></span>
      <span class="social__dot"></span>
      <span class="social__dot"></span>
    </div>
  </section>
</body>
</html>
```